Company brochure for Kestrel & Varden Works, Inc.

We need a company brochure that lets referral sources know who we are, where are locations are and what services we offer. Our website is www.kandvworksinc.com and we are on Facebook and Instagram. We need the brochure to feature both braces and prosthetics.

```html
<!DOCTYPE html>
<html lang="en">
<head>
<meta charset="utf-8">
<title>Kestrel &amp; Varden Works, Inc. — Brochure</title>
<link rel="stylesheet" href="https://fonts.googleapis.com/css2?family=Montserrat:wght@600;700;800&family=Open+Sans:wght@400;600;700&display=swap">
<style>
:root{
  --navy:#123a64;
  --blue:#17507f;
  --blue-deep:#0d2f52;
  --orange:#e8541c;
  --ink:#2b2b2b;
  --paper:#ffffff;
  --stage:#e8e8e8;
  --heading:"Montserrat",Arial,sans-serif;
  --body:"Open Sans",Arial,sans-serif;
}
*{box-sizing:border-box;margin:0;padding:0}
html,body{width:1200px;height:3303px;overflow:hidden}
body{background:var(--stage);font-family:var(--body);color:var(--ink);position:relative}
.spread{position:absolute;left:60px;width:1080px;height:839px;display:flex;box-shadow:0 6px 18px rgba(0,0,0,.25);background:var(--paper)}
.spread--outside{top:640px}
.spread--inside{top:1860px}
.panel{position:relative;width:360px;height:100%;overflow:hidden}
.panel--text{padding:38px 30px 0 32px;background:var(--paper)}
.panel--mission{background:linear-gradient(180deg,#17507f 0%,#0f3f6b 100%);color:#fff;padding:40px 30px 0 32px}
.panel--cover,.panel--lists,.panel--upper{background:var(--paper)}
h2.title{font-family:var(--heading);font-weight:800;font-size:25px;color:var(--navy);letter-spacing:.5px;margin-bottom:12px}
.panel--mission h2.title{color:#fff}
h3.sub{font-family:var(--body);font-weight:400;font-size:17px;color:var(--orange);margin:14px 0 6px}
p{font-size:9.3px;line-height:1.32;text-align:justify;margin-bottom:9px}
.panel--mission p{color:#e8f0f7}
.swoosh{position:absolute;left:0;bottom:0;width:100%;height:150px}
.location{margin-top:8px}
.pill{display:block;background:var(--orange);color:#fff;font-weight:700;font-size:10px;text-align:center;border-radius:10px;padding:3px 0;margin:0 10px 5px}
.loc-line{display:flex;align-items:flex-start;gap:6px;font-size:9.3px;line-height:1.3;color:#fff;margin-bottom:2px;padding-left:12px}
.loc-line b{font-weight:700}
.ico{flex:0 0 9px;height:9px;border-radius:50%;background:#fff;margin-top:2px;position:relative}
.ico::after{content:"";position:absolute;inset:2.5px;border-radius:50%;background:var(--blue)}
.fax{margin-left:14px;display:inline-flex;gap:6px;align-items:flex-start}
.site{position:absolute;bottom:26px;left:0;right:0;text-align:center;font-weight:700;font-size:14px;color:#fff}
.brand{position:absolute;top:34px;left:0;right:0;text-align:center}
.brand-mark{display:inline-block;width:46px;height:46px;border-radius:50%;background:var(--navy)}
.brand-name{display:block;font-family:var(--body);font-weight:700;font-size:11px;color:var(--blue);margin-top:10px}
.photo{position:absolute;background:linear-gradient(160deg,#e9eef3 0%,#b9c9d8 50%,#5f7fa6 100%)}
.cover-photo{top:150px;left:0;width:360px;height:420px}
.cover-band{position:absolute;left:0;bottom:0;width:100%;height:330px}
.cover-text{position:absolute;left:0;right:0;bottom:60px;text-align:center;color:#fff;font-family:var(--heading)}
.cover-text .l1{font-size:27px;font-weight:800;color:var(--blue-deep)}
.cover-text .l2{font-size:21px;font-weight:700;line-height:1.2}
.cover-text .site-cover{display:block;font-family:var(--body);font-size:13px;font-weight:700;margin-top:22px}
.panel--lists{padding:34px 22px 0 22px}
.panel--upper{padding:34px 22px 0 26px}
h3.cat{font-family:var(--heading);font-weight:700;font-size:15px;color:var(--navy);margin:18px 0 6px}
h3.cat:first-child{margin-top:0}
h4.group{font-family:var(--body);font-weight:400;font-size:14px;color:var(--orange);margin:8px 0 5px;line-height:1.15}
ul.ticks{list-style:none;display:grid;grid-template-columns:1fr 1fr;column-gap:10px;row-gap:4px}
ul.ticks.three{grid-template-columns:1fr 1fr 1fr}
ul.ticks.one{grid-template-columns:1fr}
ul.ticks li{position:relative;font-size:8.3px;line-height:1.2;padding-left:14px}
ul.ticks li::before{content:"";position:absolute;left:0;top:0;width:8px;height:8px;border:1.3px solid var(--blue);border-radius:50%}
ul.ticks li::after{content:"";position:absolute;left:2.6px;top:2px;width:2px;height:3.5px;border:solid var(--blue);border-width:0 1.2px 1.2px 0;transform:rotate(45deg)}
.cols{display:flex;gap:12px}
.cols>div{flex:1}
.team-photo{left:0;bottom:70px;width:360px;height:190px;background:linear-gradient(180deg,#f2f4f6 0%,#c9d4df 45%,#2f5e8e 100%)}
.upper-band{position:absolute;left:0;bottom:0;width:100%;height:120px}
.site-inside{position:absolute;bottom:24px;left:0;right:0;text-align:center;color:#fff;font-weight:700;font-size:14px}
</style>
</head>
<body>

<section class="spread spread--outside">
  <article class="panel panel--text">
    <h2 class="title">ABOUT US</h2>
    <p>Kestrel &amp; Varden Works has been providing quality, compassionate care to residents of the region since 1983. A recognized leader in the field, our experts work as a team to create the most functional solution to your orthotic, prosthetic and pedorthic needs using the latest technology available. Our patient-centered, team approach means we work closely with your doctor, nurse, therapist and family to create custom made solutions that work for you.</p>
    <p>Our practitioners make up the largest and most experienced O &amp; P practice in the area. We have both adult and pediatric specialists. Our board-certified practitioners regularly attend and conduct continuing education programs and clinics allowing us to bring our patients the very latest in technology and developments in the field. Our central Fabrication Facility allows us to fabricate your device with speed, quality, and convenience.</p>
    <h3 class="sub">Emergency 24/7 Service</h3>
    <p>Our staff is available 24 hours a day, 7 days a week for emergencies that cannot wait until the next business day. At K&amp;V Works, we are dedicated to providing the very best patient experience.</p>
    <p>With seven patient care centers to choose from, there is one near you. Call for an appointment today.</p>
    <h3 class="sub">Prosthetic Services</h3>
    <p>There are approximately 2 million people living with limb loss in the United States. Most limb loss occurs in those with compromised vascular systems, frequently because of complications from diabetes. Other causes of limb loss include cancer, traumatic injuries, or congenital disorders.</p>
    <p>At Kestrel &amp; Varden Works, we understand how devastating it is to lose a limb, and we are proud to be able to help our patients regain their function and self-confidence. The loss of a limb or the birth of a child with a limb difference doesn't have to be a limitation; it could be the beginning of a powerful new life. We at K&amp;V Works want to become part of your journey in a life without limitations. By working as a team and being a partner in the process, we can achieve your goals with a good fitting prosthesis that you need and deserve.</p>
    <p>Within our experienced team of prosthetists, we can design, fit, and fabricate a custom prostheses that is right for you.</p>
    <svg class="swoosh" viewBox="0 0 360 150" preserveAspectRatio="none" aria-hidden="true">
      <path d="M0 70 C120 40 260 40 360 28 L360 150 L0 150Z" fill="#e8541c"/>
      <path d="M0 84 C120 56 260 54 360 42 L360 150 L0 150Z" fill="#fff"/>
      <path d="M0 96 C120 68 260 66 360 56 L360 150 L0 150Z" fill="#123a64"/>
    </svg>
  </article>

  <article class="panel panel--mission">
    <h2 class="title">OUR MISSION</h2>
    <p>We are people committed to using every scientific and technical development available to restore the physical capabilities of the disabled. By combining intellectual know-how and modern technology we seek to help the "disabled" become "enabled".</p>
    <p>Our pledge is to use all of our orthotic and prosthetic resources to empower individuals with physical challenges to participate in all facets of life.</p>

    <div class="location">
      <span class="pill">Main Lab and Central Fabrication Facility:</span>
      <div class="loc-line"><span class="ico"></span>412 Larkmoor Ave. Fenwick Grove, MO 63000</div>
      <div class="loc-line"><span class="ico"></span>Phone: <b>(555) 210-4400</b><span class="fax"><span class="ico"></span>Fax: <b>(555) 210-4499</b></span></div>
      <div class="loc-line"><span class="ico"></span>Monday through Friday - <b>8:30 AM to 4:30 PM</b></div>
    </div>
    <div class="location">
      <span class="pill">Harbor Patient Care Center:</span>
      <div class="loc-line"><span class="ico"></span>Harbor Medical Pavilion 1800 Quill Place,<br>Suite 4B Fenwick, MO 63010</div>
      <div class="loc-line"><span class="ico"></span>Phone: <b>(555) 318-2200</b><span class="fax"><span class="ico"></span>Fax: <b>(555) 318-2299</b></span></div>
      <div class="loc-line"><span class="ico"></span>Monday through Friday - <b>8:30 AM to 4:30 PM</b></div>
    </div>
    <div class="location">
      <span class="pill">West County Patient Care Center:</span>
      <div class="loc-line"><span class="ico"></span>260 Old Ridge Rd, Suite 8<br>West Fenwick, MO 63020</div>
      <div class="loc-line"><span class="ico"></span>Phone: <b>(555) 427-3300</b><span class="fax"><span class="ico"></span>Fax: <b>(555) 427-3399</b></span></div>
      <div class="loc-line"><span class="ico"></span>Monday through Friday - <b>8:30 AM to 4:30 PM</b></div>
    </div>
    <div class="location">
      <span class="pill">Illinois Patient Care Center:</span>
      <div class="loc-line"><span class="ico"></span>9 Amber Court, Suite 2 Marlow, Illinois 62000</div>
      <div class="loc-line"><span class="ico"></span>Phone: <b>(555) 536-4400</b><span class="fax"><span class="ico"></span>Fax: <b>(555) 536-4499</b></span></div>
      <div class="loc-line"><span class="ico"></span>Tuesday, Wednesday &amp; Friday - <b>8:30 AM to 4:30 PM</b></div>
    </div>
    <div class="location">
      <span class="pill">Thornbury Patient Care Center:</span>
      <div class="loc-line"><span class="ico"></span>5120 Thornbury Drive, Ste. 30 Ashford, MO 63030</div>
      <div class="loc-line"><span class="ico"></span>Phone: <b>(555) 645-5500</b><span class="fax"><span class="ico"></span>Fax: <b>(555) 645-5599</b></span></div>
      <div class="loc-line"><span class="ico"></span>Monday through Friday - <b>8:30 AM to 4:30 PM</b></div>
    </div>
    <div class="location">
      <span class="pill">Central Billing Address for all Locations</span>
      <div class="loc-line"><span class="ico"></span>412 Larkmoor Ave. Fenwick Grove, MO 63000</div>
      <div class="loc-line"><span class="ico"></span>Phone: <b>(555) 210-4400</b><span class="fax"><span class="ico"></span>Fax: <b>(555) 210-4480</b></span></div>
      <div class="loc-line"><span class="ico"></span>Monday through Friday - 8:30 AM to 4:30 PM</div>
    </div>
    <div class="site">www.kandvworksinc.com</div>
  </article>

  <article class="panel panel--cover">
    <div class="brand">
      <span class="brand-mark"></span>
      <span class="brand-name">Kestrel &amp; Varden Works, Inc.</span>
    </div>
    <div class="photo cover-photo" role="img" aria-label="Photo of two smiling babies, one wearing a blue cranial helmet"></div>
    <svg class="cover-band" viewBox="0 0 360 330" preserveAspectRatio="none" aria-hidden="true">
      <path d="M0 60 C110 10 250 0 360 6 L360 330 L0 330Z" fill="#e8541c"/>
      <path d="M0 78 C110 30 250 20 360 26 L360 330 L0 330Z" fill="#fff"/>
      <path d="M0 92 C110 46 250 36 360 40 L360 330 L0 330Z" fill="#17507f"/>
      <path d="M0 300 C120 280 250 250 360 180 L360 330 L0 330Z" fill="#0f3f6b"/>
    </svg>
    <div class="cover-text">
      <div class="l1">WELCOME TO</div>
      <div class="l2">KESTREL &amp; VARDEN<br>WORKS</div>
      <span class="site-cover">www.kandvworksinc.com</span>
    </div>
  </article>
</section>

<section class="spread spread--inside">
  <article class="panel panel--text">
    <h3 class="sub" style="margin-top:0">Orthotic Services</h3>
    <p>After receiving a prescription from your physician for an orthopedic brace, you will most likely be referred to an orthotist, orthotic company or clinic team. An Orthotist is a trained healthcare professional who specializes in making a wide range of custom fit braces. It is the orthotists job to cast, measure, build, fit, maintain, and educate you on the proper wear and care of your brace. Often your physician will make the referral to a clinic team. Orthotic clinical teams for children are especially important because of changes in growth and development. This team is made up of the physician, nurse, orthotist and therapist all working together to achieve the best possible outcome. Remember the most important member and contributor to the team is YOU.</p>
    <p>The goal of orthotic bracing is different for each patient. The goals could involve increasing your mobility, decrease a hospital stay, supporting a week or deformed limb, reducing fatigue, picking up you toe as you walk, stopping the progression of a spinal curve, maintain correction of a foot, protecting a new surgery or fixing a flat spot on a child's head. Whatever the problem area is, our orthotists are experts in wide variety bracing solutions.</p>
    <p>Kestrel and Varden Works | PCB Accredited</p>
    <p>At Kestrel &amp; Varden Works, our facilities are PCB accredited and our orthotic staff is made up of certified professionals. We have both adult and pediatric specialist, so you can be sure that the right orthotist is a member of your team.</p>
    <h3 class="sub" style="margin-top:40px">PCB Accredited Facility</h3>
    <p>Did you know that in most states there are no requirements for education, certification or licensure for orthotists, prosthetists or pedorthists? Take a proactive approach in determining who you will be working with - being informed will only help you gain a positive outcome. It's important that you choose a highly qualified, rigorously trained individual, someone who has the appropriate education and training and is PCB certified in their discipline. Choosing an PCB accredited facility is also just as important. PCB's exacting standards ensure that PCB accredited facilities have earned the mark of exceptional quality and superior patient care. You deserve nothing less.</p>
    <p>Kestrel &amp; Varden Works is an PCB Certified Facility staffed with PCB certified professional who can help you reach your goals. Certification and accreditation provides you with the assurance that the right practitioner is a member of your team.</p>
    <svg class="swoosh" viewBox="0 0 360 150" preserveAspectRatio="none" aria-hidden="true">
      <path d="M0 50 C90 110 250 100 360 84 L360 150 L0 150Z" fill="#e8541c"/>
      <path d="M0 66 C90 122 250 112 360 98 L360 150 L0 150Z" fill="#fff"/>
      <path d="M0 78 C90 132 250 122 360 110 L360 150 L0 150Z" fill="#123a64"/>
    </svg>
  </article>

  <article class="panel panel--lists">
    <h3 class="cat">CRANIAL</h3>
    <ul class="ticks three">
      <li>Cranial Remolding Orthoses</li>
      <li>Custom Post-Surgical Helmets</li>
      <li>Protective Helmets</li>
    </ul>
    <h3 class="cat">CERVICAL</h3>
    <ul class="ticks">
      <li>Wire Foam Collar</li><li>Alder /Coral Collars</li>
      <li>Molded Plastic Collar</li><li>HALO</li>
      <li>Semi Rigid Collar</li><li>Non Invasive Halo</li>
      <li>SOMI</li><li>Torticollis Orthoses</li>
    </ul>
    <h3 class="cat">LOWER EXTREMITY ORTHOSIS</h3>
    <h4 class="group">Foot Orthotics</h4>
    <ul class="ticks"><li>Foot Orthoses</li><li>UCBL Orthoses</li></ul>
    <h4 class="group">Ankle Foot Orthoses (AFO)</h4>
    <ul class="ticks">
      <li>Ankle Supports</li><li>CAM Walker</li>
      <li>Prefabricated AFO's</li><li>Pressure Relief AFO</li>
      <li>Total Carbon Fiber AFO's</li><li>Tibial Fracture Brace</li>
      <li>Solid Ankle AFO's</li><li>Tibial Torsion Orthosis</li>
      <li>Posterior Leaf Spring AFO's</li><li>Dynamic ROM AFO</li>
      <li>Metal Double Upright AFO's</li><li>Plantar Fasciitis Splint</li>
      <li>Ground Reaction AFO's</li><li>Contour Restraint Walker</li>
      <li>Spiral Carbon Fiber AFO's</li><li>Sonora AFO</li>
    </ul>
    <h4 class="group">Knee Ankle Foot Orthoses</h4>
    <ul class="ticks">
      <li>Knee Patella Supports</li><li>Femoral Fracture Braces</li>
      <li>Knee Immobilizers</li><li>ACL / PCL Knee Braces</li>
      <li>ROM Knee Braces</li><li>OA Knee Braces</li>
      <li>Single Upright KAFO's</li><li>Swedish KO</li>
      <li>Double Upright KAFO's</li><li>Dynamic ROM KAFO / KO's</li>
    </ul>
    <div class="cols">
      <div>
        <h4 class="group">Hip Knee Ankle Foot</h4>
        <ul class="ticks one">
          <li>HKAFO Femoral Fx Brace</li><li>Custom HKAFO</li>
          <li>Reciprocating Gait Orthoses</li><li>Standing Frame</li>
          <li>A-Frame</li><li>Parapodium</li>
        </ul>
      </div>
      <div>
        <h4 class="group">Hip Orthoses</h4>
        <ul class="ticks one">
          <li>Adjustable Hip Abduction</li><li>Pembury Harness</li>
          <li>Rover or Glider Hip Braces</li><li>Static Hip Abduction Braces</li>
          <li>Highland Rite</li><li>SWIFT Orthosis</li>
          <li>Dynamic Hip Abduction</li>
        </ul>
      </div>
    </div>
  </article>

  <article class="panel panel--upper">
    <h3 class="cat">UPPER EXTREMITY</h3>
    <div class="cols">
      <div>
        <h4 class="group">Wrist Hand<br>Orthoses</h4>
        <ul class="ticks one">
          <li>Wrist Cock Up</li><li>Resting Hand Splint</li>
          <li>Custom Molded WHO</li><li>Dynamic Finger Splint</li>
          <li>Dynamic Hand Finger Splint</li><li>Dynamic Wrist Hand Finger Splint</li>
          <li>Tenodesis Splint</li><li>Dynamic Range of Motion WHO</li>
        </ul>
      </div>
      <div>
        <h4 class="group">Shoulder-Elbow<br>Orthoses</h4>
        <ul class="ticks one">
          <li>Shoulder Abduction Harness</li><li>Clavicle Sling</li>
          <li>Static Elbow Orthoses</li><li>Articulating Elbow Orthoses</li>
          <li>Dynamic Range of Motion Elbow</li><li>Ulnar Fracture Orthoses</li>
          <li>Humeral Fracture Orthose</li>
        </ul>
      </div>
    </div>
    <h4 class="group" style="margin-top:14px">Pediatric Corrective</h4>
    <ul class="ticks">
      <li>Marlow Straight Last Shoes</li><li>Easy Reach Bars</li>
      <li>Dalton Clubfoot Bars</li><li>Wexford Brace</li>
      <li>Dunmore Splints</li>
    </ul>
    <h3 class="cat">SPINAL</h3>
    <div class="cols">
      <div>
        <h4 class="group">Spinal/Thoracic</h4>
        <ul class="ticks one">
          <li>LS Corset</li><li>Chairback LSO</li><li>Custom Molded LSO</li>
          <li>Hyperextension TLSO</li><li>TLSO Corset</li><li>Custom Molded TLSO</li>
        </ul>
      </div>
      <div>
        <h4 class="group">Spine/Scoliosis</h4>
        <ul class="ticks one">
          <li>Scoliosis TLSO</li><li>Millbrook CTLSO</li>
        </ul>
      </div>
    </div>
    <div class="photo team-photo" role="img" aria-label="Photo of the clinical team standing in a row in white coats and scrubs"></div>
    <svg class="upper-band" viewBox="0 0 360 120" preserveAspectRatio="none" aria-hidden="true">
      <path d="M0 20 C120 50 250 40 360 10 L360 120 L0 120Z" fill="#17507f"/>
    </svg>
    <div class="site-inside">www.kandvworksinc.com</div>
  </article>
</section>

</body>
</html>
```